Landingpage design for Movarabroker website

We need a design for a responsive 1 page landing page.
Good example: https://www.kelvaro.com/
On the homepage we will like to have a explanation video
attached you can find the logo's

About the website Movara.offers:
Movara.offers is a “Broker” we bring buyers and sellers together and facilitate transactions

Simple
quickly
Actuel
Compare (who is the best provider, at what price)
great offer
independent
1 invoice

Target Market(s)

BtoB

Number of Pages Required

1 page

Requirements
Must have
• On the homepage we will like to have a explanation video
Nice to have
• something between shipper and carrier and bring them togheter
• We will focus us first on fish transport... maybe you can add something
• Map from europe that shows our workarea

```html
<!DOCTYPE html>
<html lang="en">
<head>
<meta charset="utf-8">
<title>Movara Offers – Landing page</title>
<link href="https://fonts.googleapis.com/css2?family=Roboto:wght@400;500;700&display=swap" rel="stylesheet">
<style>
:root{
  --blue:#1ea7dc;
  --blue-dark:#1690c2;
  --ink:#1a1a1a;
  --text:#333333;
  --grey-bg:#f4f4f4;
  --grey-shape:#e4e4e4;
  --btn-grey:#d6d6d6;
  --footer:#050505;
  --white:#ffffff;
}
*{margin:0;padding:0;box-sizing:border-box}
html,body{width:1200px;height:3416px;overflow:hidden}
body{position:relative;font-family:'Roboto',Arial,sans-serif;color:var(--text);background:var(--white)}
.abs{position:absolute}

/* header + hero */
.hero-photo{left:340px;top:91px;width:860px;height:535px;background:linear-gradient(135deg,#3b4550 0%,#1d232a 45%,#0e1114 100%)}
.hero-blue{left:0;top:0;width:1200px;height:626px;background:linear-gradient(160deg,#2bb3e6,var(--blue) 60%,var(--blue-dark));clip-path:polygon(0 0,352px 0,547px 626px,0 626px)}
.logo{left:78px;top:22px;display:flex;align-items:center;gap:12px;color:var(--white);font-weight:700;font-size:22px;line-height:1.05;text-transform:uppercase}
.logo-dot{width:40px;height:40px;border-radius:50%;background:var(--white)}
.nav{left:364px;top:37px;display:flex;gap:0}
.nav a{position:absolute;font-size:14px;font-weight:500;color:var(--ink);text-decoration:none;white-space:nowrap}
.btn-login{left:756px;top:27px;width:102px;height:37px;background:var(--blue);color:var(--white);display:flex;align-items:center;justify-content:center;gap:10px;font-size:13px;font-weight:700}
.btn-register{left:872px;top:27px;width:123px;height:37px;border:2px solid var(--ink);color:var(--ink);display:flex;align-items:center;justify-content:center;gap:10px;font-size:13px;font-weight:700}
.btn-search{left:1006px;top:27px;width:46px;height:37px;border:2px solid var(--ink);display:flex;align-items:center;justify-content:center}
.btn-menu{left:1075px;top:27px;width:46px;height:37px;border:2px solid var(--blue);display:flex;align-items:center;justify-content:center}

.video{left:80px;top:205px;width:471px;height:289px;background:#222;border:1px solid #555}
.video-still{position:absolute;left:0;top:0;width:100%;height:251px;background:linear-gradient(150deg,#8c9aa6 0%,#d9dfe4 40%,#6d7780 100%)}
.video-bar{position:absolute;left:0;bottom:0;width:100%;height:38px;background:#151515;display:flex;align-items:center;padding:0 14px;gap:14px}
.play{position:absolute;left:205px;top:95px;width:62px;height:62px;border-radius:50%;background:rgba(0,0,0,.55);display:flex;align-items:center;justify-content:center}
.track{width:250px;height:6px;background:#555;position:relative}
.track i{position:absolute;left:0;top:0;height:6px;width:200px;background:var(--blue)}
.track b{position:absolute;left:194px;top:-5px;width:16px;height:16px;border-radius:50%;background:#ddd}
.vol{width:80px;height:4px;background:#666;position:relative;margin-left:14px}
.vol b{position:absolute;left:30px;top:-9px;width:22px;height:22px;border-radius:50%;background:#ddd}

.hero-title{left:667px;top:198px;color:var(--white);font-size:24px;font-weight:700;line-height:34px}
.hero-box{left:667px;top:289px;width:449px;height:105px;background:rgba(0,0,0,.85);color:var(--white);font-size:13px;line-height:18px;padding:17px 10px}
.hero-box p+p{margin-top:12px}
.hero-cta{left:667px;top:410px;width:312px;height:54px;background:#000;border-right:4px solid var(--blue);color:var(--white);font-size:13px;font-weight:700;line-height:18px;padding:9px 12px}

/* content sections */
.section{left:0;width:1200px;height:492px;overflow:hidden}
.section.light{background:var(--grey-bg)}
.section.white{background:var(--white)}
.deco-grey{position:absolute;inset:0;background:linear-gradient(200deg,#efefef,var(--grey-shape));clip-path:polygon(62% 0,100% 0,100% 100%,56% 100%,80% 55%)}
.deco-blue{position:absolute;inset:0;background:linear-gradient(150deg,#35b8ea,var(--blue) 55%,var(--blue-dark));clip-path:polygon(0 0,330px 0,535px 100%,0 100%)}
.media{position:absolute;top:84px;width:485px;height:326px;border:1px solid #999}
.light .media{left:633px}
.white .media{left:80px}
.copy{position:absolute;top:112px;width:444px}
.light .copy{left:80px}
.white .copy{left:653px}
.copy h2{font-size:24px;font-weight:700;color:var(--ink);padding-bottom:12px;border-bottom:1px solid #9bcfe6}
.copy p{margin-top:14px;font-size:13px;line-height:19px;color:var(--text)}
.cta{display:block;margin-top:18px;width:312px;height:54px;background:var(--btn-grey);border-right:4px solid #8a9aa5;color:var(--ink);font-size:13px;font-weight:700;line-height:18px;padding:9px 16px}

/* footer */
.footer{left:0;top:3088px;width:1200px;height:282px;background:var(--footer);color:var(--white)}
.footer h3{position:absolute;top:50px;font-size:14px;font-weight:700;text-transform:uppercase;padding-bottom:12px;border-bottom:1px solid #444}
.footer h3 span{color:var(--blue)}
.quick{position:absolute;left:80px;top:98px;list-style:none;font-size:12px;line-height:34px}
.quick li::before{content:"";display:inline-block;width:5px;height:5px;border-radius:50%;background:var(--white);margin-right:8px;vertical-align:middle}
.contact{position:absolute;left:300px;top:96px;font-size:12px;line-height:17px}
.contact .row{display:flex;gap:12px;margin-bottom:12px}
.contact svg{flex:none;margin-top:2px}
.map-thumb{position:absolute;left:631px;top:96px;width:250px;height:132px;border:3px solid #666;background:linear-gradient(135deg,#e8e4da,#cfd6c8)}
.foot-logo{position:absolute;left:986px;top:116px;display:flex;align-items:center;gap:10px;font-size:20px;font-weight:700;text-transform:uppercase}
.foot-logo i{width:30px;height:30px;border-radius:50%;background:var(--white)}
.social{position:absolute;left:986px;top:194px;display:flex;gap:11px}
.social span{width:23px;height:23px;background:var(--blue)}
.copyright{left:0;top:3370px;width:1200px;height:46px;background:var(--blue);color:var(--ink);font-size:12px;text-align:center;line-height:46px}
</style>
</head>
<body>

<div class="abs hero-photo" role="img" aria-label="Photo of a delivery truck on a road at dusk"></div>
<div class="abs hero-blue"></div>

<header>
  <div class="abs logo"><span class="logo-dot"></span><span>Movara<br>Offers</span></div>
  <nav>
    <a class="abs" style="left:364px;top:37px" href="#about">ABOUT US</a>
    <a class="abs" style="left:467px;top:37px" href="#pricing">PRICING</a>
    <a class="abs" style="left:558px;top:37px" href="#faq">FAQ</a>
    <a class="abs" style="left:622px;top:37px" href="#contact">CONTACT</a>
  </nav>
  <div class="abs btn-login">
    <svg width="16" height="16" viewBox="0 0 16 16" fill="none" stroke="#fff" stroke-width="2"><path d="M9 2h5v12H9"/><path d="M2 8h8M7 5l3 3-3 3"/></svg>LOGIN
  </div>
  <div class="abs btn-register">
    <svg width="16" height="16" viewBox="0 0 16 16" fill="none" stroke="#1a1a1a" stroke-width="2"><path d="M2 3h7M2 3v11h11V8"/><path d="M6 10l1-3 6-6 2 2-6 6z"/></svg>REGISTER
  </div>
  <div class="abs btn-search">
    <svg width="18" height="18" viewBox="0 0 18 18" fill="none" stroke="#1a1a1a" stroke-width="2.5"><circle cx="7.5" cy="7.5" r="5.5"/><path d="M12 12l5 5"/></svg>
  </div>
  <div class="abs btn-menu">
    <svg width="22" height="16" viewBox="0 0 22 16" stroke="#1ea7dc" stroke-width="2.5"><path d="M0 2h22M0 8h22M0 14h22"/></svg>
  </div>
</header>

<section class="hero">
  <div class="abs video">
    <div class="video-still" role="img" aria-label="Explanation video still showing a refrigerated truck being loaded"></div>
    <div class="play"><svg width="22" height="24" viewBox="0 0 22 24"><path d="M2 1l19 11L2 23z" fill="#fff"/></svg></div>
    <div class="video-bar">
      <svg width="12" height="14" viewBox="0 0 12 14" fill="#fff"><rect x="0" y="0" width="4" height="14"/><rect x="8" y="0" width="4" height="14"/></svg>
      <div class="track"><i></i><b></b></div>
      <svg width="16" height="14" viewBox="0 0 16 14" fill="#bbb"><rect y="0" width="16" height="3"/><rect y="5.5" width="16" height="3"/><rect y="11" width="16" height="3"/></svg>
      <div class="vol"><b></b></div>
    </div>
  </div>
  <h1 class="abs hero-title">Looking for a transport company?<br>Looking for a looking?</h1>
  <div class="abs hero-box">
    <p>We bring you together and find the best and most efficient way for your shipments.</p>
    <p>Movara Offers is FREE</p>
  </div>
  <div class="abs hero-cta">You are a view steps away from the<br>easiest way to organize your transports!</div>
</section>

<section class="abs section light" style="top:626px" id="about">
  <div class="deco-grey"></div>
  <div class="copy">
    <h2>why should i use Movara offers?</h2>
    <p>Lorem ipsum dolor sit amet, consectetuer adipiscing elit, sed diam nonummy nibh euismod tincidunt ut laoreet dolore magna aliquam erat volutpat. Ut wisi enim ad minim veniam, quis nostrud exerci tation ullamcorper suscipit lobortis nisl ut aliquip ex ea commodo consequat.</p>
    <span class="cta">You are a view steps away from the<br>easiest way to organize your transports!</span>
  </div>
  <div class="media" role="img" aria-label="Illustration of an egg linked to a farm, a hen house and a map of Europe" style="background:radial-gradient(circle at 50% 60%,#d88a5a 0,#c9774a 18%,#eeeeee 30%,#dcdcdc 100%)"></div>
</section>

<section class="abs section white" style="top:1118px" id="pricing">
  <div class="deco-blue"></div>
  <div class="media" role="img" aria-label="Photo of a man opening large blue insulated fish containers" style="background:linear-gradient(120deg,#a9a9a2 0%,#7f8a96 35%,#3f7fd0 60%,#2f66b8 100%)"></div>
  <div class="copy">
    <h2>Transport solutions</h2>
    <p>Lorem ipsum dolor sit amet, consectetuer adipiscing elit, sed diam nonummy nibh euismod tincidunt ut laoreet dolore magna aliquam erat volutpat. Ut wisi enim ad minim veniam, quis nostrud exerci tation ullamcorper suscipit lobortis nisl ut aliquip ex ea commodo consequat.</p>
    <span class="cta">You are a view steps away from the<br>easiest way to organize your transports!</span>
  </div>
</section>

<section class="abs section light" style="top:1610px">
  <div class="deco-grey"></div>
  <div class="copy">
    <h2>Destanition Europe</h2>
    <p>Lorem ipsum dolor sit amet, consectetuer adipiscing elit, sed diam nonummy nibh euismod tincidunt ut laoreet dolore magna aliquam erat volutpat. Ut wisi enim ad minim veniam, quis nostrud exerci tation ullamcorper suscipit lobortis nisl ut aliquip ex ea commodo consequat.</p>
    <span class="cta">You are a view steps away from the<br>easiest way to organize your transports!</span>
  </div>
  <div class="media" role="img" aria-label="Dotted map of the work area with three blue location pins" style="background:radial-gradient(circle at 50% 50%,#d8d8d8,#9c9c9c)"></div>
</section>

<section class="abs section white" style="top:2102px" id="faq">
  <div class="deco-blue"></div>
  <div class="media" role="img" aria-label="Green price tag labelled free on a light blurred background" style="background:radial-gradient(circle at 45% 55%,#8cc63f 0,#7ab32e 22%,#e9eef2 40%,#d6dde3 100%)"></div>
  <div class="copy">
    <h2>Free?</h2>
    <p>Lorem ipsum dolor sit amet, consectetuer adipiscing elit, sed diam nonummy nibh euismod tincidunt ut laoreet dolore magna aliquam erat volutpat. Ut wisi enim ad minim veniam, quis nostrud exerci tation ullamcorper suscipit lobortis nisl ut aliquip ex ea commodo consequat.</p>
    <span class="cta">You are a view steps away from the<br>easiest way to organize your transports!</span>
  </div>
</section>

<section class="abs section light" style="top:2594px;height:494px" id="contact">
  <div class="deco-grey"></div>
  <div class="copy">
    <h2>Contact</h2>
    <p>Lorem ipsum dolor sit amet, consectetuer adipiscing elit, sed diam nonummy nibh euismod tincidunt ut laoreet dolore magna aliquam erat volutpat. Ut wisi enim ad minim veniam, quis nostrud exerci tation ullamcorper suscipit lobortis nisl ut aliquip ex ea commodo consequat.</p>
    <span class="cta">You are a view steps away from the<br>easiest way to organize your transports!</span>
  </div>
  <div class="media" role="img" aria-label="Road map of central and eastern Europe" style="background:linear-gradient(160deg,#e9e6dc 0%,#dfe3cf 55%,#a9cde8 100%)"></div>
</section>

<footer class="abs footer">
  <h3 style="left:80px">Quick <span>Links</span></h3>
  <ul class="quick">
    <li>About Us</li>
    <li>Pricing</li>
    <li>Faq</li>
    <li>Contact</li>
  </ul>

  <h3 style="left:300px">Contact <span>Details</span></h3>
  <div class="contact">
    <div class="row">
      <svg width="12" height="15" viewBox="0 0 12 15"><path d="M6 0a6 6 0 0 1 6 6c0 4-6 9-6 9S0 10 0 6a6 6 0 0 1 6-6z" fill="#1ea7dc"/><circle cx="6" cy="6" r="2" fill="#050505"/></svg>
      <div><strong>Movara Offers</strong><br>Sed ut perspiciatis unde omnis<br>iste natus errorluptatem</div>
    </div>
    <div class="row">
      <svg width="13" height="13" viewBox="0 0 13 13"><path d="M3 0l2 3-1.5 1.5a8 8 0 0 0 5 5L10 8l3 2-1.5 3C6 13 0 7 0 1.5z" fill="#1ea7dc"/></svg>
      <div>0123 456 789</div>
    </div>
    <div class="row">
      <svg width="14" height="11" viewBox="0 0 14 11"><rect width="14" height="11" fill="#1ea7dc"/><path d="M0 0l7 6 7-6" fill="none" stroke="#050505" stroke-width="1.5"/></svg>
      <div>info@movaraoffers.com</div>
    </div>
  </div>

  <h3 style="left:626px">Location <span>Map</span></h3>
  <div class="map-thumb" role="img" aria-label="Street map of the office location"></div>

  <div class="foot-logo"><i></i>Movara Offers</div>
  <div class="social" aria-label="Social links"><span></span><span></span><span></span><span></span></div>
</footer>

<div class="abs copyright">Copyright © 2017 Movara Offers. All Rights Reserved</div>

</body>
</html>
```